Web design required

1-We need a web design for existing company based in New Zealand
2-We build residential house and light commercial
3-We has in-house designer which allow us can provide interior design
4-We modeling project before site construction, which enable both client and construction team to visually analysis whole project,

Target Market(s)

middle class residential house market
Ref: http://www.brackwellbuilders.co.nz/

Industry/Entity Type

Construction Company

Number of Pages Required

1 page

Font styles to use
Sans Serif
Other font styles liked:
• Such as : Central Gothic or similar which has more design taste

Colors

Designer to choose colors to be used in the design.

Requirements
Must have
• Front sheet, contact information, sample project

```html
<!DOCTYPE html>
<html lang="en">
<head>
<meta charset="utf-8">
<title>Harbourline Homes</title>
<link href="https://fonts.googleapis.com/css2?family=Jost:wght@400;500;600;700&display=swap" rel="stylesheet">
<style>
:root{
  --blue:#1a64ad;
  --blue-light:#2f86d4;
  --dark:#1c1d1f;
  --dark-2:#2a2c30;
  --ink:#222;
  --muted:#555;
  --line:#d9d9d9;
  --white:#fff;
}
*{margin:0;padding:0;box-sizing:border-box}
html,body{width:1200px;height:3879px;overflow:hidden;background:#fff}
body{font-family:"Jost",sans-serif;color:var(--ink);position:relative}
.abs{position:absolute}
.topbar{top:0;left:0;width:1200px;height:40px;}
.topbar .contact{position:absolute;right:80px;top:8px;display:flex;gap:26px;font-size:15px;color:#fff;z-index:3}
.topbar .contact span{display:flex;align-items:center;gap:8px}
.topbar .bg{position:absolute;right:0;top:0;width:470px;height:40px;background:var(--blue);clip-path:polygon(30px 0,100% 0,100% 100%,0 100%)}
.header{top:40px;left:0;width:1200px;height:96px;background:#fff}
.brand{position:absolute;left:88px;top:20px;display:flex;align-items:center;gap:12px;font-weight:600;font-size:26px;letter-spacing:5px;color:var(--dark)}
.brand .dot{width:40px;height:40px;border-radius:50%;background:var(--blue)}
.nav{position:absolute;right:80px;top:42px;display:flex;gap:56px;font-size:14px;font-weight:500;text-transform:uppercase;color:var(--ink)}
.nav .active{color:var(--blue)}
.hero{top:136px;left:0;width:1200px;height:540px;clip-path:polygon(0 0,100% 0,100% 470px,50% 540px,0 470px);
  background:linear-gradient(180deg,#8ea6be 0%,#7a6f62 40%,#4d4a40 75%,#3a3d2c 100%)}
.hero-text{top:410px;left:92px;background:rgba(0,0,0,.72);padding:12px 16px;color:#fff;font-size:30px;font-weight:600;line-height:1.15}
.btn{display:inline-flex;align-items:center;height:34px;padding:0 18px;background:var(--blue);color:#fff;font-size:14px;font-weight:500;text-transform:uppercase}
.btn-dark{background:var(--dark);color:#fff}
.hero .btn{position:absolute}
.dots{top:676px}
.section-title{width:1200px;left:0;text-align:center;font-weight:600;font-size:36px;text-transform:uppercase;letter-spacing:1px}
.section-title .hl{color:var(--blue)}
.rule{left:88px;width:1024px;height:1px;background:var(--line)}
.rule-badge{left:588px;width:24px;height:24px;border-radius:50%;background:var(--blue)}
.welcome-text{top:912px;left:88px;width:1024px;text-align:center;font-size:15px;line-height:2.05;color:var(--muted)}
.pill{display:flex;align-items:center}
.pill .c{width:34px;height:34px;border-radius:50%;background:var(--blue);margin-right:-6px;position:relative;z-index:1}
.services{top:1150px;left:0;width:1200px;height:570px;background:linear-gradient(180deg,#2b2d31,#1a1b1d);clip-path:polygon(0 0,100% 0,100% 460px,50% 570px,0 460px)}
.card{top:1313px;width:444px;height:264px;background:rgba(26,100,173,.82);border:3px solid #fff;color:#fff;text-align:center;padding:30px 28px}
.card .icon{width:84px;height:90px;margin:0 auto 14px;background:#fff;clip-path:polygon(50% 0,100% 25%,100% 75%,50% 100%,0 75%,0 25%)}
.card h3{font-size:20px;font-weight:600;margin-bottom:8px}
.card p{font-size:13px;line-height:1.55}
.hex{width:258px;height:292px;clip-path:polygon(50% 0,100% 25%,100% 75%,50% 100%,0 75%,0 25%)}
.hex.first{background:#222;color:#fff;padding:112px 40px 0;text-align:center}
.hex.first h4{font-size:17px;font-weight:600;text-transform:uppercase}
.hex.first p{font-size:13px;line-height:1.4}
.cta{top:2508px;left:0;width:1200px;height:290px;background:linear-gradient(180deg,#2a2c30,#1b1c1e);clip-path:polygon(0 0,100% 0,100% 220px,50% 290px,0 220px);color:#fff;text-align:center}
.cta h2{margin-top:58px;font-size:34px;font-weight:600;text-transform:uppercase}
.cta p{width:960px;margin:14px auto 0;font-size:14px;line-height:1.75;color:#ddd}
.blog-card{top:2987px;width:321px;height:323px;background:#fff;border:1px solid #e5e5e5}
.blog-card .photo{height:174px;position:relative}
.blog-card .date{position:absolute;left:12px;bottom:-16px;width:50px;height:50px;background:var(--blue);color:#fff;font-size:14px;font-weight:600;text-align:center;line-height:1.1;padding-top:8px}
.blog-card h4{margin:32px 12px 6px;font-size:14px;font-weight:600;line-height:1.3}
.blog-card p{margin:0 12px;font-size:12px;line-height:1.5;color:var(--muted)}
.footer{top:3362px;left:0;width:1200px;height:473px;background:linear-gradient(180deg,#2b2d31,#18191b);clip-path:polygon(50% 0,100% 70px,100% 100%,0 100%,0 70px);color:#fff}
.footer-brand{position:absolute;left:0;width:1200px;top:92px;text-align:center;font-size:30px;font-weight:600;letter-spacing:8px}
.footer-brand .dot{width:56px;height:56px;border-radius:50%;background:#fff;margin:0 auto 14px}
.fcol{position:absolute;top:232px;width:300px;text-align:center;font-size:14px;line-height:1.4}
.fcol h5{color:var(--blue-light);font-size:24px;font-weight:500;margin-bottom:4px}
.fnav{position:absolute;top:345px;left:0;width:1200px;display:flex;justify-content:center;gap:62px;font-size:13px;text-transform:uppercase}
.fnav .active{color:var(--blue-light)}
.social{position:absolute;top:400px;left:0;width:1200px;display:flex;justify-content:center;gap:10px}
.social span{width:28px;height:28px;border-radius:50%;background:var(--blue)}
.copy{top:3835px;left:0;width:1200px;height:44px;background:var(--blue);color:#fff;font-size:13px;text-align:center;line-height:44px}
</style>
</head>
<body>
<div class="abs topbar"><div class="bg"></div>
  <div class="contact">
    <span><svg width="18" height="18" viewBox="0 0 24 24"><circle cx="12" cy="12" r="11" fill="none" stroke="#fff" stroke-width="1.6"/><path d="M8 6l2 3-1 1.5a7 7 0 0 0 4.5 4.5L15 14l3 2-1.5 2A10 10 0 0 1 6 7.5z" fill="#fff"/></svg>123-456-7890</span>
    <span><svg width="18" height="18" viewBox="0 0 24 24"><circle cx="12" cy="12" r="11" fill="none" stroke="#fff" stroke-width="1.6"/><rect x="6" y="8" width="12" height="8" fill="none" stroke="#fff" stroke-width="1.4"/><path d="M6 8l6 5 6-5" fill="none" stroke="#fff" stroke-width="1.4"/></svg>info@harbourlinehomes.co.nz</span>
  </div>
</div>
<header class="abs header">
  <div class="brand"><span class="dot"></span>HARBOURLINE</div>
  <nav class="nav"><span class="active">Home</span><span>About Us</span><span>Services</span><span>Portfolio</span><span>Blog</span><span>Contact</span></nav>
</header>

<section class="abs hero" role="img" aria-label="Photo of a two-storey stone and weatherboard family home with autumn trees"></section>
<div class="abs hero-text">We are light commercial and<br>residential houses Construction</div>
<span class="abs btn" style="top:496px;left:98px;height:30px;font-size:13px">Read More</span>
<svg class="abs" style="top:676px;left:560px" width="80" height="14"><circle cx="20" cy="7" r="5" fill="#ccc"/><circle cx="40" cy="7" r="5" fill="var(--blue)"/><circle cx="60" cy="7" r="5" fill="#ccc"/></svg>

<h2 class="abs section-title" style="top:796px">Welcome to <span class="hl">Harbourline</span></h2>
<div class="abs rule" style="top:880px"></div>
<div class="abs rule-badge" style="top:868px"></div>
<p class="abs welcome-text">Lorem Ipsum is simply dummy text of the printing and typesetting industry. Lorem Ipsum has been the industry's standard dummy text ever since the 1500s, when an unknown printer took a galley of type and scrambled it to make a type specimen book. It has survived not only five centuries, but also the leap into electronic typesetting, remaining essentially unchanged. It was popularised in the 1960s with the release of Typeline sheets containing Lorem Ipsum passages, and more recently with desktop publishing software like PageForm including versions of Lorem Ipsum.</p>
<div class="abs pill" style="top:1058px;left:528px"><span class="c"></span><span class="btn btn-dark">Read More</span></div>

<section class="abs services" role="img" aria-label="Dark photo of houses at dusk"></section>
<h2 class="abs section-title" style="top:1194px;color:#fff">Our Services</h2>
<div class="abs rule" style="top:1266px;background:#666"></div>
<div class="abs rule-badge" style="top:1254px;background:#fff"></div>
<div class="abs card" style="left:134px"><div class="icon"></div><h3>Light Commercial</h3><p>Lorem ipsum dolor sit amet, consectetuer adipiscing elit, sed diam nonummy nibh euismod tincidunt ut laoreet dolore magna aliquam erat volutpat. Ut wisi enim ad minim veniam, quis nostrud exerci tation ullamcorper suscipit lobortis nisl ut aliquip.</p></div>
<div class="abs card" style="left:620px"><div class="icon"></div><h3>Residential House</h3><p>Lorem ipsum dolor sit amet, consectetuer adipiscing elit, sed diam nonummy nibh euismod tincidunt ut laoreet dolore magna aliquam erat volutpat. Ut wisi enim ad minim veniam, quis nostrud exerci tation ullamcorper suscipit lobortis nisl ut aliquip.</p></div>

<h2 class="abs section-title" style="top:1766px">Our <span class="hl">Projects</span></h2>
<div class="abs rule" style="top:1836px"></div>
<div class="abs rule-badge" style="top:1824px"></div>
<div class="abs hex first" style="top:1861px;left:78px"><h4>Lorem Ipsum Dolor</h4><p>Lorem ipsum dolor sit amet, consectetuer adipis cing.</p></div>
<div class="abs hex" style="top:1861px;left:339px;background:linear-gradient(180deg,#5d8fd1,#8a6a4a 60%,#5d7a3d)" role="img" aria-label="Project photo: timber-clad family home"></div>
<div class="abs hex" style="top:1861px;left:600px;background:linear-gradient(180deg,#7aa8df,#c9b995 55%,#6f8a4f)" role="img" aria-label="Project photo: two-storey suburban house"></div>
<div class="abs hex" style="top:1861px;left:861px;background:linear-gradient(180deg,#6b8fb8,#4a3d33 55%,#8a5a35)" role="img" aria-label="Project photo: modern home with deck at dusk"></div>
<div class="abs hex" style="top:2094px;left:208px;background:linear-gradient(180deg,#4f86cf,#d8d8d4 55%,#4e7a3a)" role="img" aria-label="Project photo: single-level home with garage"></div>
<div class="abs hex" style="top:2094px;left:469px;background:linear-gradient(180deg,#3c4c8a,#c99a3e 50%,#5a4a3a)" role="img" aria-label="Project photo: lit glass commercial building"></div>
<div class="abs hex" style="top:2094px;left:730px;background:linear-gradient(180deg,#5e90d4,#b9866a 50%,#9a9a9a)" role="img" aria-label="Project photo: brick commercial building"></div>
<div class="abs pill" style="top:2417px;left:528px"><span class="c"></span><span class="btn btn-dark">View More</span></div>

<section class="abs cta" role="img" aria-label="Dark photo of a house exterior">
  <h2>Lorem Ipsum Dolor Sit Amet Consectetuer</h2>
  <p>Duis autem vel eum iriure dolor in hendrerit in vulputate velit esse molestie consequat, vel illum dolore eu feugiat nulla facilisis at vero eros et accumsan et iusto odio dig quis nostrud exerci tation ullamcorper suscipit lobortis nisl ut aliquip ex ea commodo consequat.</p>
</section>
<div class="abs pill" style="top:2698px;left:514px"><span class="c"></span><span class="btn">Call Us Today</span></div>

<h2 class="abs section-title" style="top:2874px">Latest <span class="hl">Blog</span></h2>
<div class="abs rule" style="top:2944px"></div>
<div class="abs rule-badge" style="top:2932px"></div>
<article class="abs blog-card" style="left:88px"><div class="photo" style="background:linear-gradient(180deg,#6ea6e0,#cfc3a6 55%,#6d8f4a)" role="img" aria-label="Row of two-storey houses"><div class="date">02<br>Nov</div></div><h4>Lorem ipsum amet, consectetuer adipiscing elit</h4><p>Lorem ipsum dolor sit amet, consectetuer adipiscing elit, sed diam nonummy nibh euismod tincidunt ut laoreet dolore magna erat volutpat...[+]</p></article>
<article class="abs blog-card" style="left:440px"><div class="photo" style="background:linear-gradient(180deg,#2f6fc4,#e2e0dc 55%,#5b8a3c)" role="img" aria-label="Single-level home with garage"><div class="date">02<br>Nov</div></div><h4>Lorem ipsum amet, consectetuer adipiscing elit</h4><p>Lorem ipsum dolor sit amet, consectetuer adipiscing elit, sed diam nonummy nibh euismod tincidunt ut laoreet dolore magna erat volutpat...[+]</p></article>
<article class="abs blog-card" style="left:791px"><div class="photo" style="background:linear-gradient(180deg,#4d8fdb,#b88a6c 55%,#8f8f8a)" role="img" aria-label="Terrace of brick townhouses"><div class="date">02<br>Nov</div></div><h4>Lorem ipsum amet, consectetuer adipiscing elit</h4><p>Lorem ipsum dolor sit amet, consectetuer adipiscing elit, sed diam nonummy nibh euismod tincidunt ut laoreet dolore magna erat volutpat...[+]</p></article>

<footer class="abs footer" role="img" aria-label="Dark photo of a residential street">
  <div class="footer-brand"><div class="dot"></div>HARBOURLINE</div>
  <div class="fcol" style="left:127px"><h5>VISIT</h5>123-Lorem ipsum dolor sit amet,<br>consectetuer, CA-123456</div>
  <div class="fcol" style="left:447px"><h5>CALL</h5>123-456-7890</div>
  <div class="fcol" style="left:768px"><h5>EMAIL</h5>info@harbourlinehomes.co.nz</div>
  <nav class="fnav"><span class="active">Home</span><span>About Us</span><span>Services</span><span>Portfolio</span><span>Blog</span><span>Contact</span></nav>
  <div class="social"><span></span><span></span><span></span><span></span></div>
</footer>
<div class="abs copy">Copyright © 2017 Harbourline Homes Construction. All Rights Reserved.</div>
</body>
</html>
```